Re-design my Shearing Contract Estimate format.

The one page contract estimate is the output of a Farmer going online to our website and creating their shearing contract estimate.
The design should follow our current branding.
I have uploaded the current contract estimate design and a screen shot of our home page

```html
<!DOCTYPE html>
<html lang="en">
<head>
<meta charset="utf-8">
<title>Shearing Contract Estimate</title>
<link href="https://fonts.googleapis.com/css2?family=Noto+Sans:wght@400;700&display=swap" rel="stylesheet">
<style>
  :root {
    --bg: #f1f1f1;
    --paper: #ffffff;
    --brand-dark: #5f8a70;
    --band: #5bd69c;
    --band-bright: #5de6a6;
    --rule: #8a8a8a;
    --ink: #111111;
    --label-on-band: #ffffff;
    --faint: #c9c9c9;
  }
  * { box-sizing: border-box; margin: 0; padding: 0; }
  html, body { width: 1200px; height: 1200px; overflow: hidden; }
  body {
    background: var(--bg);
    font-family: "Noto Sans", sans-serif;
    color: var(--ink);
  }
  .estimate-page {
    position: absolute;
    left: 137px; top: 0;
    width: 926px; height: 1200px;
    background: var(--paper);
  }
  .brand {
    position: absolute;
    left: 0; right: 0; top: 88px;
    display: flex; align-items: center; justify-content: center; gap: 10px;
    color: var(--brand-dark);
    font-weight: 700;
    font-size: 40px;
    letter-spacing: 1px;
  }
  .brand-dot {
    width: 22px; height: 22px; border-radius: 50%;
    background: var(--brand-dark);
  }
  .field-label {
    position: absolute; top: 256px; height: 25px; width: 133px;
    background: var(--band);
    color: var(--label-on-band);
    font-weight: 700; font-size: 13.5px;
    line-height: 25px; padding-left: 18px;
  }
  .field-label.grower { padding-left: 6px; }
  .field-tab {
    position: absolute; top: 256px; width: 12px; height: 14px;
    background: var(--band);
  }
  .field-input {
    position: absolute; top: 256px; height: 25px; width: 236px;
    border: 1.5px solid var(--rule);
  }
  .section-title {
    position: absolute; left: 71px; width: 777px; height: 23px;
    background: var(--band-bright);
    text-align: center;
    font-weight: 700; font-size: 15px; line-height: 24px;
  }
  .section-title.muted { background: var(--band); }
  .section-tab {
    position: absolute; left: 78px; width: 17px; height: 13px;
    background: var(--band);
  }
  .estimate-table {
    position: absolute; left: 71px; width: 777px;
    border-collapse: collapse;
    font-size: 14.5px;
  }
  .estimate-table td {
    height: 23.5px;
    border: 1px solid var(--rule);
    padding: 0 0 0 21px;
    line-height: 1;
    vertical-align: bottom;
    padding-bottom: 2px;
  }
  .estimate-table td.value { width: 184px; padding: 0; }
  .estimate-table .strong td { font-weight: 700; }
  .footer-mark {
    position: absolute; left: 135px; top: 1110px;
    color: var(--faint);
    font-weight: 700; font-size: 14px;
  }
</style>
</head>
<body>
<main class="estimate-page">
  <header class="brand">
    <span class="brand-dot"></span>
    <span class="brand-name">Ridgeline</span>
  </header>

  <div class="field-label" style="left:71px">Contract No.</div>
  <div class="field-tab" style="left:207px"></div>
  <div class="field-input" style="left:220px"></div>
  <div class="field-label grower" style="left:462px">Grower Details</div>
  <div class="field-tab" style="left:598px"></div>
  <div class="field-input" style="left:611px"></div>

  <h2 class="section-title muted" style="top:357px">Sheep / Shearing Type</h2>
  <div class="section-tab" style="top:384px"></div>
  <table class="estimate-table" style="top:396px">
    <tr class="strong"><td>Merinos</td><td class="value"></td></tr>
    <tr class="strong"><td>XB Ewes</td><td class="value"></td></tr>
    <tr class="strong"><td>Lambs</td><td class="value"></td></tr>
    <tr class="strong"><td>Full Crutch</td><td class="value"></td></tr>
    <tr class="strong"><td>Mkt Crutch</td><td class="value"></td></tr>
    <tr class="strong"><td>Rams</td><td class="value"></td></tr>
    <tr class="strong"><td>Total Number of Sheep</td><td class="value"></td></tr>
    <tr class="strong"><td>Number of Shed Stands</td><td class="value"></td></tr>
  </table>

  <h2 class="section-title" style="top:619px">Wool Staff Requirements</h2>
  <div class="section-tab" style="top:646px"></div>
  <table class="estimate-table" style="top:658px">
    <tr><td>Wool Handler</td><td class="value"></td></tr>
    <tr><td>Wool Classer</td><td class="value"></td></tr>
    <tr><td>Wool Presser / Penner (Combined Role)</td><td class="value"></td></tr>
    <tr><td>Wool Presser</td><td class="value"></td></tr>
    <tr><td>Penner</td><td class="value"></td></tr>
  </table>

  <h2 class="section-title" style="top:809px">Estimated Contract Prcie</h2>
  <div class="section-tab" style="top:836px"></div>
  <table class="estimate-table" style="top:848px">
    <tr><td>Total Shearing Contract Cost</td><td class="value"></td></tr>
    <tr><td>Total Wool Staff Contract Cost</td><td class="value"></td></tr>
    <tr class="strong"><td>Total Exl GST</td><td class="value"></td></tr>
    <tr class="strong"><td>Total Inc GST</td><td class="value"></td></tr>
    <tr><td>Total Estimated per Sheep</td><td class="value"></td></tr>
  </table>

  <footer class="footer-mark">Ridgeline</footer>
</main>
</body>
</html>
```